Popup Nightclub Grand Opening Flyer

We need to design a flyer for the grand opening of an upscale, exclusive nightclub called "Lanternfall". The design needs to be chic and exclusive. The background should be black and the text should primarily be white. We like minimalist designs.

Here is the text for the flyer
-
Velvetrope Atlanta Presents

Lanternfall (LOGO)

A Popup Nightclub Experience
For one night Only

Friday, October 18, 2013
Party begins at 9PM

INVITE ONLY

See invitation for location details
(Velvetrope Atlanta logo)

-
Examples we like

http://cdn2-b.brivelpost.com/sites/default/files/styles/image_content_width/hash/3d/fa/1472093815_4471_flyer.jpg?itok=R8kqWm2z

http://api.plovra.com/files/7Kqq-Tr82XXB3pQzJvmtR5HL2W719E4nbRtC6KLd4HsfM8Y2qTDK-VmjwDoNqLX4QBzTHD9nakRbVx3m-Pfq8htc3MDTWr5p4/2zelSaturdays.jpg

http://quenmar.com/wp-content/uploads/yootheme/widgetkit/gallery/2zel/2zel-gen_vroom4-01.jpg

Hi All, one thing that we are seeing that we don't like is on over emphasis on the phrase "a popup nightclub experience" please don't make this the largest thing on the flyer

Target Market(s)

Target market is 25-35 year olds who are affluent (rich) and like luxury brands

Requirements
Must have
• Dark Background
Nice to have
• Velvetrope Logo on the bottom
Modern text that isn't curvy
Should not have
• Curved text

```html
<!DOCTYPE html>
<html lang="en">
<head>
<meta charset="utf-8">
<title>Lanternfall Nightclub – Popup Night</title>
<link rel="stylesheet" href="https://fonts.googleapis.com/css2?family=Oswald:wght@600;700&family=Raleway:wght@100;300;400;500&family=Arimo:wght@400&display=swap">
<style>
  :root {
    --ink: #000000;
    --paper: #ffffff;
    --pattern-dark: #0b0b0b;
    --pattern-mid: #262626;
    --muted: #d9d9d9;
    --ribbon-tail: #c4c4c4;
    --ribbon-fold: #7a7a7a;
  }
  * { margin: 0; padding: 0; box-sizing: border-box; }
  html, body {
    width: 776px; height: 1200px; overflow: hidden; background: var(--ink);
  }
  .flyer {
    position: relative; width: 776px; height: 1200px; overflow: hidden;
    color: var(--paper); text-align: center;
    font-family: "Raleway", sans-serif;
  }
  .flyer__backdrop {
    position: absolute; inset: 0;
    background: radial-gradient(ellipse at 50% 40%, var(--pattern-mid) 0%, var(--pattern-dark) 70%, var(--ink) 100%);
  }
  .line { position: absolute; left: 0; width: 100%; white-space: nowrap; line-height: 1; }

  .presenter { top: 60px; font-size: 22px; font-weight: 500; letter-spacing: 1.5px; }

  .brand-mark {
    position: absolute; left: 333px; top: 122px; width: 110px; height: 110px;
    border: 3px solid var(--muted); border-radius: 50%;
  }
  .brand-name { top: 262px; font-size: 72px; font-weight: 300; letter-spacing: 6px; }
  .brand-sub  { top: 348px; font-size: 24px; font-weight: 300; letter-spacing: 3px; }

  .headline { font-family: "Oswald", sans-serif; font-weight: 700; text-transform: uppercase; letter-spacing: -0.5px; }
  .headline--a { top: 402px; font-size: 54px; }
  .headline--b { top: 464px; font-size: 62px; letter-spacing: -1px; }
  .headline--c { top: 534px; font-size: 56px; }

  .tagline { top: 640px; font-size: 24px; font-weight: 400; letter-spacing: 4px; }

  .rule { position: absolute; height: 3px; background: var(--paper); }
  .rule--top { left: 150px; width: 476px; top: 750px; }
  .rule--bottom { left: 170px; width: 436px; top: 896px; }

  .date { top: 782px; font-size: 48px; }
  .date__day { font-family: "Raleway", sans-serif; font-weight: 100; letter-spacing: -1px; }
  .date__main { font-family: "Oswald", sans-serif; font-weight: 600; font-size: 46px; }

  .start-time { top: 848px; font-size: 30px; font-weight: 400; }

  .access-ribbon { position: absolute; left: 170px; top: 938px; width: 436px; height: 70px; }
  .access-label {
    top: 952px; font-family: "Arimo", sans-serif; font-size: 34px; color: var(--ink);
  }

  .directions { top: 1034px; font-size: 18px; font-weight: 400; letter-spacing: 4px; }

  .host { position: absolute; left: 0; top: 1064px; width: 100%; display: flex; justify-content: center; align-items: center; gap: 22px; }
  .host__square { width: 64px; height: 64px; border: 3px solid var(--paper); }
  .host__divider { width: 2px; height: 80px; background: var(--paper); }
  .host__name { text-align: left; font-weight: 300; line-height: 1; }
  .host__word { display: block; font-size: 44px; letter-spacing: 1px; }
  .host__city { display: block; font-size: 16px; letter-spacing: 2px; margin-top: 6px; }
</style>
</head>
<body>
<main class="flyer">
  <div class="flyer__backdrop" role="img" aria-label="Black background with a subtle dark grey damask swirl pattern"></div>

  <p class="line presenter">VELVETROPE ATLANTA PRESENTS</p>

  <div class="brand-mark" aria-hidden="true"></div>
  <h1 class="line brand-name">LANTERNFALL</h1>
  <p class="line brand-sub">NIGHTCLUB</p>

  <h2 class="line headline headline--a">A Popup</h2>
  <h2 class="line headline headline--b">Nightclub</h2>
  <h2 class="line headline headline--c">Experience</h2>

  <p class="line tagline">FOR ONE NIGHT ONLY</p>

  <div class="rule rule--top"></div>
  <p class="line date"><span class="date__day">FRIDAY</span><span class="date__main">, OCTOBER 18, 2013</span></p>
  <p class="line start-time">PARTY BEGINS AT 9PM</p>
  <div class="rule rule--bottom"></div>

  <svg class="access-ribbon" viewBox="0 0 436 70" aria-hidden="true">
    <polygon points="0,18 62,18 62,66 0,66 20,42" fill="var(--ribbon-tail)"/>
    <polygon points="436,18 374,18 374,66 436,66 416,42" fill="var(--ribbon-tail)"/>
    <polygon points="44,58 62,66 62,58" fill="var(--ribbon-fold)"/>
    <polygon points="392,58 374,66 374,58" fill="var(--ribbon-fold)"/>
    <rect x="44" y="4" width="348" height="54" fill="var(--paper)"/>
  </svg>
  <p class="line access-label">INVITE ONLY</p>

  <p class="line directions">SEE INVITATION FOR LOCATION DETAILS</p>

  <div class="host">
    <div class="host__square" aria-hidden="true"></div>
    <div class="host__divider" aria-hidden="true"></div>
    <p class="host__name"><span class="host__word">VELVETROPE</span><span class="host__city">ATLANTA</span></p>
  </div>
</main>
</body>
</html>
```